Classy, Elegant, Simple Business Card Design

Looking to have a classy, simple, and elegant design. Want a top notch designed business card. I really like the look of the new brivo credit card. I also like the design I attached. I am trying to reach 21-29 year old females for booking us for there wedding or event. We offer Disc Jockey Service, Photo Booth Rentals, and Uplighting .

Target Market(s)

21-28 year old females

Contact Information for Business Card

Has to have logo, website, email, and phone number

Font styles to use
Other font styles liked:
• open to font choice, modern, clean
Designer to choose
33a6d7
0791cd
0555a3
ffffff

Requirements
Must have
• Has to have logo, website, email, and phone number
Nice to have
• I really like the design of the new brivo credit card. I also included my logo and some designs I like
Should not have
• clutter or too much info

```html
<!DOCTYPE html>
<html lang="en">
<head>
<meta charset="utf-8">
<title>Tidewell Event Group – Business Card</title>
<link href="https://fonts.googleapis.com/css2?family=Poppins:wght@300;400;500;600&display=swap" rel="stylesheet">
<style>
  :root{
    --sky:#33a6d7;
    --bright:#0791cd;
    --royal:#0555a3;
    --navy:#133e6e;
    --white:#ffffff;
    --stage:#1c1c1e;
    --muted:#7a8a9c;
  }
  *{margin:0;padding:0;box-sizing:border-box}
  html,body{width:1200px;height:885px;overflow:hidden}
  body{background:var(--stage);font-family:"Poppins",sans-serif;position:relative}
  .card{position:absolute;width:700px;height:400px;border-radius:4px;overflow:hidden;box-shadow:0 18px 40px rgba(0,0,0,.5)}
  .card-back{left:60px;top:38px;background:radial-gradient(ellipse at 55% 55%,var(--bright) 0%,var(--sky) 45%,#1a84c8 100%);display:flex;align-items:center;justify-content:center}
  .card-back .brand-large{color:var(--royal);font-weight:600;font-size:64px;letter-spacing:6px}
  .card-front{left:440px;top:447px;background:var(--white)}
  .card-front .wave{position:absolute;inset:0}
  .contact-block{position:absolute;left:56px;top:110px;color:var(--white)}
  .person-name{font-size:26px;font-weight:600;line-height:1.1}
  .person-title{font-size:15px;font-weight:300;margin-bottom:18px}
  .contact-list{list-style:none;font-size:15px;font-weight:400;line-height:1.55}
  .contact-list li{display:flex;align-items:center;gap:12px}
  .contact-list svg{width:16px;height:16px;flex:none}
  .service-list{margin-top:20px;font-size:15px;line-height:1.5;padding-left:18px}
  .brand-block{position:absolute;right:46px;top:120px;display:flex;flex-direction:column;align-items:flex-start}
  .brand-row{display:flex;align-items:center;gap:10px}
  .brand-dot{width:18px;height:18px;border-radius:50%;background:var(--bright)}
  .brand-name{color:var(--royal);font-weight:600;font-size:34px;letter-spacing:2px}
  .brand-sub{color:var(--muted);font-weight:300;font-size:12px;letter-spacing:6px;margin-top:2px;padding-left:30px}
</style>
</head>
<body>
  <section class="card card-back">
    <span class="brand-large">TIDEWELL</span>
  </section>

  <section class="card card-front">
    <svg class="wave" viewBox="0 0 700 400" preserveAspectRatio="none" aria-hidden="true">
      <path d="M0 0 H355 C340 60 420 110 450 180 C485 260 490 330 480 400 H0 Z" fill="var(--navy)"/>
      <path d="M355 0 C345 55 410 100 445 170 C480 250 490 330 480 400" fill="none" stroke="var(--bright)" stroke-width="6"/>
      <path d="M368 0 C360 50 420 95 456 165 C492 245 500 330 492 400" fill="none" stroke="var(--sky)" stroke-width="2"/>
    </svg>

    <div class="contact-block">
      <div class="person-name">Daniel Reyes</div>
      <div class="person-title">President</div>
      <ul class="contact-list">
        <li><svg viewBox="0 0 16 16"><path d="M3 2h3l1 3-2 1a8 8 0 0 0 5 5l1-2 3 1v3a1 1 0 0 1-1 1A12 12 0 0 1 2 3a1 1 0 0 1 1-1z" fill="var(--white)"/></svg>555-214-7730</li>
        <li><svg viewBox="0 0 16 16"><rect x="1" y="3" width="14" height="10" rx="1" fill="var(--white)"/><path d="M1 4l7 5 7-5" fill="none" stroke="var(--navy)" stroke-width="1.4"/></svg>info@tidewellevents.com</li>
        <li><svg viewBox="0 0 16 16"><circle cx="8" cy="8" r="7" fill="var(--white)"/><path d="M1 8h14M8 1c-3 4-3 10 0 14M8 1c3 4 3 10 0 14" fill="none" stroke="var(--navy)" stroke-width="1.1"/></svg>www.tidewellevents.com</li>
      </ul>
      <ul class="service-list">
        <li>Disc Jockey Service</li>
        <li>Photo Booth Rentals</li>
        <li>Uplighting</li>
      </ul>
    </div>

    <div class="brand-block">
      <div class="brand-row"><span class="brand-dot"></span><span class="brand-name">TIDEWELL</span></div>
      <div class="brand-sub">EVENT GROUP</div>
    </div>
  </section>
</body>
</html>
```